design a web site for Halvern Link Works

Require a web site for a new business. We design, implement and manage high level and highly secure IT solutions for high end corporates and large government departments. we specialize in Secure Fibre optic products for highly secure LAN environments and data centre expertise

Target Market(s)

High end corporates and large government departments

Industry/Entity Type

IT

Coding

Coded - Design and coding required

Number of Pages Required

5+ page

Font styles to use
Other font styles liked:
• Calibri

Colors
0054AA
0677BA
7BADD7
CADEEF
E8F1F8
EB3D1F
EC4F4E
F09395
F8D3D4
FCEDEE

Requirements
Must have
• High end tech look and feel needs to incorporate the HLW Company Logo Three major sections. Basic all day Fibre solutions for everyone. High end solutions for blue chip customers. And high secure solutions for sensitive customers
Nice to have
• Online catalogue
Should not have
• Mundane or outdated look and feel

```html
<!DOCTYPE html>
<html lang="en">
<head>
<meta charset="utf-8">
<title>Halvern Link Works — Trusted Network Solutions</title>
<link href="https://fonts.googleapis.com/css2?family=Audiowide&family=Poppins:wght@400;500;600;700&display=swap" rel="stylesheet">
<style>
:root{
  --navy:#1b2f6e;
  --navy-dark:#142559;
  --blue:#0054aa;
  --red:#c8202f;
  --red-bright:#e0283a;
  --ink:#1d1d2b;
  --muted:#555a66;
  --pale:#eef0f4;
  --white:#ffffff;
  --display:'Audiowide', sans-serif;
  --body:'Poppins', sans-serif;
}
*{box-sizing:border-box;margin:0;padding:0}
html,body{width:1200px;height:5319px;overflow:hidden}
body{position:relative;background:var(--white);font-family:var(--body);color:var(--ink)}
.abs{position:absolute}
.display{font-family:var(--display);text-transform:uppercase;line-height:1.05}
.red{color:var(--red)} .navy{color:var(--navy)}
.btn{position:absolute;display:flex;align-items:center;justify-content:center;background:var(--red);color:#fff;font-family:var(--display);text-transform:uppercase;border-radius:30px;font-size:14px;box-shadow:0 4px 10px rgba(200,32,47,.35)}
.photo{position:absolute}

/* top bar + nav */
.topbar-text{position:absolute;top:11px;color:#fff;font-family:var(--display);font-size:11px;letter-spacing:.5px}
.nav a{position:absolute;top:63px;font-family:var(--display);font-size:11.5px;color:var(--ink);text-decoration:none;text-transform:uppercase}
.nav a.active{color:var(--red)}
.nav a.active::after{content:"";position:absolute;left:0;right:0;bottom:-6px;height:2px;background:var(--red)}
.brand{position:absolute;display:flex;align-items:center;gap:8px;font-family:var(--display);text-transform:uppercase;white-space:nowrap}
.brand .mark{display:block;background:var(--red)}

/* about */
.about-text{position:absolute;left:607px;top:1026px;width:432px;font-size:13.5px;line-height:23px;color:var(--muted);text-align:justify}

/* customers */
.card{position:absolute;top:1751px;width:302px;height:386px;background:#fff;box-shadow:0 6px 20px rgba(0,0,0,.08);padding:32px 38px}
.card.featured{background:var(--red);color:#fff}
.card h3{font-size:17px;font-weight:600;line-height:23px;margin-top:18px;text-transform:uppercase;color:var(--navy)}
.card.featured h3{color:#fff}
.card p{font-size:13px;line-height:20px;margin-top:16px;color:var(--muted)}
.card ul{margin-top:20px;list-style:none;font-size:13px;line-height:28px;color:var(--navy)}
.card li::before{content:"•";margin-right:10px}
.card.featured p,.card.featured ul{color:#fff}

/* products */
.product{position:absolute;top:3027px;width:303px;height:384px;background:#fff;box-shadow:0 6px 18px rgba(0,0,0,.1);text-align:center}
.product .thumb{position:relative;height:230px}
.product .play{position:absolute;left:50%;top:50%;width:50px;height:36px;margin:-18px 0 0 -25px;background:#e00;border-radius:10px}
.product .play::after{content:"";position:absolute;left:20px;top:10px;border-left:14px solid #fff;border-top:8px solid transparent;border-bottom:8px solid transparent}
.product h4{margin-top:30px;font-size:18px;font-weight:600;text-transform:uppercase;color:var(--navy)}
.product p{margin:12px 30px 0;font-size:13px;line-height:20px;color:var(--muted)}

/* blog */
.post{position:absolute;left:547px;width:393px;height:140px;background:#fff;border-radius:0 70px 70px 0;box-shadow:6px 4px 14px rgba(0,0,0,.08);padding:34px 30px 0 55px}
.post h5{font-family:var(--display);font-size:14px;line-height:17px;color:var(--navy);text-transform:uppercase}
.post p{font-size:11px;line-height:15px;color:var(--muted);margin-top:8px}
.post-thumb{position:absolute;left:956px;width:132px;height:132px;border-radius:50%}

/* footer */
.foot-h{position:absolute;font-family:var(--display);font-size:20px;color:#fff;text-transform:uppercase;letter-spacing:1px}
.field{position:absolute;background:#fff;font-size:12px;color:#333;padding:10px 12px}
.foot-small{position:absolute;color:#fff;font-size:12px;line-height:19px}
.links{position:absolute;left:958px;top:4945px;list-style:none;color:#fff;font-size:12px;line-height:23px}
.social{position:absolute;top:5194px;width:26px;height:26px;border-radius:50%;background:var(--red-bright)}
</style>
</head>
<body>

<!-- Top bar -->
<header>
  <svg class="abs" style="left:0;top:0" width="1200" height="37" aria-hidden="true">
    <polygon points="0,0 500,0 485,37 0,37" fill="var(--red)"/>
    <polygon points="700,0 1200,0 1200,37 715,37" fill="var(--navy)"/>
  </svg>
  <span class="topbar-text" style="left:135px">&#9742; Call us: 555 014 276</span>
  <span class="topbar-text" style="left:370px">&#9993; Email us</span>
  <span class="topbar-text" style="left:865px">Download Catalogue</span>

  <nav class="nav">
    <a href="#" class="active" style="left:145px">Home</a>
    <a href="#" style="left:228px">About us</a>
    <a href="#" style="left:347px">Our services</a>
    <a href="#" style="left:722px">Products</a>
    <a href="#" style="left:870px">Customers</a>
    <a href="#" style="left:980px">Contact</a>
  </nav>
  <div class="brand" style="left:508px;top:56px;font-size:12px;color:var(--navy)"><span class="mark" style="width:12px;height:12px"></span>Halvern Link Works</div>
</header>

<!-- Hero -->
<section>
  <div class="photo" role="img" aria-label="Close-up of network patch cables and fibre strands in deep blue light" style="left:0;top:103px;width:1200px;height:640px;background:radial-gradient(ellipse at 55% 40%,#4b6fb0 0%,#24427f 45%,#101d45 100%)"></div>
  <svg class="abs" style="left:0;top:640px" width="1200" height="103" aria-hidden="true">
    <polygon points="0,103 1200,25 1200,103" fill="var(--red)"/>
    <path d="M0,103 Q600,80 1200,70 L1200,103 Z" fill="#fff"/>
  </svg>
  <div class="brand" style="left:0;width:1200px;justify-content:center;top:420px;font-size:46px;color:#fff"><span class="mark" style="width:34px;height:34px"></span>Halvern Link Works</div>
  <div class="abs" style="left:0;width:1200px;top:515px;text-align:center;color:#fff;font-family:var(--display);font-size:14px;letter-spacing:12px">TRUSTED NETWORK SOLUTIONS</div>
</section>

<!-- About -->
<section>
  <svg class="abs" style="left:1020px;top:895px" width="180" height="60" aria-hidden="true">
    <rect x="0" y="0" width="120" height="14" rx="7" fill="#f7dcdf"/>
    <rect x="140" y="0" width="60" height="14" rx="7" fill="#e9ebf0"/>
    <rect x="40" y="30" width="140" height="14" rx="7" fill="#f7dcdf"/>
  </svg>
  <div class="abs" style="left:90px;top:848px;width:392px;height:436px;background:#fff;box-shadow:0 6px 20px rgba(0,0,0,.12)"></div>
  <div class="photo" role="img" aria-label="Two engineers reviewing equipment in a server room" style="left:99px;top:857px;width:380px;height:423px;background:linear-gradient(135deg,#7d8796,#3e4656 60%,#2a3040)"></div>
  <div class="photo" role="img" aria-label="Fibre optic patch cords plugged into a patch panel" style="left:268px;top:1094px;width:290px;height:327px;background:linear-gradient(160deg,#4f8fb5,#1f5d86 55%,#c7a24a);border:6px solid #fff"></div>
  <svg class="abs" style="left:185px;top:1295px" width="80" height="60" aria-hidden="true">
    <rect x="20" y="2" width="60" height="6" rx="3" fill="var(--red)"/><circle cx="10" cy="5" r="3" fill="var(--navy)"/>
    <rect x="30" y="22" width="50" height="6" rx="3" fill="var(--navy)"/><circle cx="20" cy="25" r="3" fill="var(--red)"/>
    <rect x="25" y="42" width="55" height="6" rx="3" fill="var(--red)"/><circle cx="15" cy="45" r="3" fill="var(--navy)"/>
  </svg>
  <h2 class="display abs" style="left:524px;top:898px;font-size:46px"><span class="navy">About Halvern</span><br><span class="red">Link Works</span></h2>
  <p class="about-text">Lorem ipsum dolor sit amet, consectetur adipiscing elit, sed do eiusmod tempor incididunt ut labore et dolore magna aliqua. Quis ipsum suspendisse ultrices gravida. Risus com modo viverra maecenas accumsan lacus vel facilisis. Lorem ipsum dolor sit amet, consectetur adipiscing elit, sed do eiusmod tempor incididunt ut labore et dolore magna aliqua. Quis ipsum suspendisse ultrices gravida. Risus commodo viverra maecenas accumsan lacus vel facilisis. Lorem ipsum dolor sit amet, consectetur adipiscing elit, sed do eiusmod tempor incididunt ut labore et dolore magna aliqua. Quis ipsum suspendisse ultrices gravida. Risus commodo viverra maecenas accumsan lacus vel facilisis.</p>
  <a class="btn" style="left:607px;top:1332px;width:153px;height:45px">Read more</a>
</section>

<!-- Customers -->
<section>
  <div class="abs" style="left:0;top:1553px;width:1200px;height:698px;background:var(--pale)"></div>
  <h2 class="display abs" style="left:0;width:1200px;text-align:center;top:1648px;font-size:46px"><span class="navy">Our</span> <span class="red">Customers</span></h2>

  <article class="card featured" style="left:114px">
    <svg width="50" height="58" viewBox="0 0 50 58" aria-hidden="true"><circle cx="25" cy="14" r="13" fill="#fff"/><path d="M2,58 Q2,32 25,32 Q48,32 48,58 Z" fill="#fff"/></svg>
    <h3>Basic all day fibre solutions for everyone</h3>
    <p>Lorem ipsum dolor sit amet, consectetur adipiscing elit, sed do eiusmod tempor incididunt</p>
    <ul><li>At labore et dolore gna</li><li>Sliquauis ipsum suspendis</li><li>Qe ultrices gravidaiscom</li></ul>
  </article>
  <article class="card" style="left:452px">
    <svg width="50" height="58" viewBox="0 0 50 58" aria-hidden="true"><circle cx="25" cy="14" r="13" fill="var(--red)"/><path d="M2,58 Q2,32 25,32 Q48,32 48,58 Z" fill="var(--red)"/></svg>
    <h3>High end solutions for blue chip customers.</h3>
    <p>Lorem ipsum dolor sit amet, consectetur adipiscing elit, sed do eiusmod tempor incididunt</p>
    <ul><li>At labore et dolore gna</li><li>Sliquauis ipsum suspendis</li><li>Qe ultrices gravidaiscom</li></ul>
  </article>
  <article class="card" style="left:793px">
    <svg width="64" height="58" viewBox="0 0 64 58" aria-hidden="true"><circle cx="12" cy="16" r="8" fill="var(--red)"/><circle cx="52" cy="16" r="8" fill="var(--red)"/><circle cx="32" cy="12" r="11" fill="var(--red)"/><path d="M0,50 Q0,28 12,28 Q24,28 24,50Z M40,50 Q40,28 52,28 Q64,28 64,50Z" fill="var(--red)"/><path d="M14,58 Q14,28 32,28 Q50,28 50,58Z" fill="var(--red)"/></svg>
    <h3>High secure solutions for sensitive customers</h3>
    <p>Lorem ipsum dolor sit amet, consectetur adipiscing elit, sed do eiusmod tempor incididunt</p>
    <ul><li>At labore et dolore gna</li><li>Sliquauis ipsum suspendis</li><li>Qe ultrices gravidaiscom</li></ul>
  </article>
</section>

<!-- What is -->
<section>
  <div class="abs" style="left:0;top:2251px;width:1200px;height:549px;background:var(--navy)"></div>
  <div class="photo" role="img" aria-label="Rack-mounted fibre switches with cables, tinted red" style="left:0;top:2251px;width:1200px;height:549px;background:linear-gradient(120deg,#a0182a,#e0283a 45%,#8c1322);clip-path:polygon(700px 0,1200px 0,1200px 549px,560px 549px)"></div>
  <svg class="abs" style="left:0;top:2251px" width="1200" height="549" aria-hidden="true">
    <polygon points="560,549 700,0 740,0 610,549" fill="#2f4aa0" opacity=".85"/>
    <polygon points="700,0 760,0 760,120" fill="var(--red)"/>
  </svg>
  <h2 class="display abs" style="left:147px;top:2333px;font-size:46px;line-height:54px;color:#fff">What is<br><span style="color:var(--red-bright)">Optical<br>Fibre LAN?</span></h2>
  <p class="abs" style="left:147px;top:2509px;width:356px;font-size:13.5px;line-height:23px;color:#fff;text-align:justify">Lorem ipsum dolor sit amet, consectetur adipiscing elit, sed do eiusmod tempor incididunt ut labore et dolore magna aliqua. Quis ipsum suspendisse ultrices gravida. Risus com modo viverra maecenas accumsan lacus vel facilisis. Lorem ipsum dolor sit amet, consectetur adipiscing elit, sed do eiusmod tempor incididunt ut labore et dolore magna aliqua.</p>
</section>

<!-- Featured products -->
<section>
  <h2 class="display abs" style="left:0;width:1200px;text-align:center;top:2925px;font-size:46px"><span class="navy">Featured</span> <span class="red">Products</span></h2>
  <article class="product" style="left:112px">
    <div class="thumb" role="img" aria-label="Blue and yellow patch cables in a network rack" style="background:linear-gradient(160deg,#2b63b8,#5d9ad8 50%,#d8c24a)"><span class="play"></span></div>
    <h4>Guardline Cable</h4>
    <p>Lorem ipsum dolor sit amet, consectetur adipiscing elit, sed do eiusmod tempor incid</p>
  </article>
  <article class="product" style="left:448px">
    <div class="thumb" role="img" aria-label="Server room corridor with blue cabling" style="background:linear-gradient(160deg,#3b2a25,#1f4a80 55%,#3e8cd0)"><span class="play"></span></div>
    <h4>Swiftpath Cable</h4>
    <p>Lorem ipsum dolor sit amet, consectetur adipiscing elit, sed do eiusmod tempor incid</p>
  </article>
  <article class="product" style="left:785px">
    <div class="thumb" role="img" aria-label="Fibre cables connected to a blue switch panel" style="background:linear-gradient(160deg,#3f7fc2,#2b5f9e 50%,#cfd24a)"><span class="play"></span></div>
    <h4>Clearlite Cable</h4>
    <p>Lorem ipsum dolor sit amet, consectetur adipiscing elit, sed do eiusmod tempor incid</p>
  </article>
</section>

<!-- Online catalogue -->
<section>
  <svg class="abs" style="left:0;top:3530px" width="1200" height="380" aria-hidden="true">
    <polygon points="0,20 130,110 130,200 0,110" fill="var(--red)"/>
    <polygon points="0,140 130,230 130,320 0,230" fill="var(--navy)"/>
    <polygon points="1200,20 1070,110 1070,200 1200,110" fill="var(--navy)"/>
    <polygon points="1200,140 1070,230 1070,320 1200,230" fill="var(--red)"/>
  </svg>
  <div class="abs" style="left:109px;top:3541px;width:979px;height:358px;background:#fff;box-shadow:0 8px 24px rgba(0,0,0,.12)"></div>
  <div class="abs" style="left:217px;top:3589px;width:202px;height:256px;background:linear-gradient(180deg,#1f3880,#15285f);box-shadow:4px 6px 14px rgba(0,0,0,.3)">
    <div class="brand" style="left:0;width:202px;justify-content:center;top:34px;font-size:7px;color:#fff"><span class="mark" style="width:6px;height:6px"></span>Halvern Link Works</div>
    <div class="abs" style="left:0;width:202px;top:115px;text-align:center;color:#fff;font-family:var(--display);font-size:13px;line-height:16px">PRODUCT<br>CATALOGUE</div>
    <div class="abs" style="left:56px;top:152px;width:90px;height:2px;background:var(--red)"></div>
  </div>
  <h2 class="display abs" style="left:494px;top:3628px;font-size:31px"><span class="navy">Online</span> <span class="red">Catalogue</span></h2>
  <p class="abs" style="left:496px;top:3673px;width:470px;font-size:12.5px;line-height:19px;color:var(--muted)">Lorem ipsum dolor sit amet, consectetur adipiscing elit, sed do eiusmod tempor incididunt ut labore et dolore magna aliqua. Quis ipsum suspendisse ultrices gravida. Risus com modo viverra m</p>
  <a class="btn" style="left:489px;top:3752px;width:192px;height:37px;font-size:12px">Download now</a>
</section>

<!-- Blog -->
<section>
  <h2 class="display abs" style="left:0;width:1200px;text-align:center;top:4062px;font-size:46px"><span class="navy">Latest</span> <span class="red">Blog Posts</span></h2>
  <div class="photo" role="img" aria-label="Technician working on cabling in a data centre" style="left:109px;top:4155px;width:415px;height:477px;background:linear-gradient(135deg,#2a4d8c,#4a6fa8 40%,#b8a597 70%,#5a6c8c)"></div>
  <article class="post" style="top:4155px"><h5>Lorem ipsum dolor sit amet, consectetur</h5><p>Lorem ipsum dolor sit amet, consectetur adipi scing elit, sed do eiusmod tempolabor</p></article>
  <div class="post-thumb" role="img" aria-label="Hands connecting fibre cables" style="top:4159px;background:linear-gradient(135deg,#c9ccd6,#57688a)"></div>
  <article class="post" style="top:4330px"><h5>Lorem ipsum dolor sit amet, consectetur</h5><p>Lorem ipsum dolor sit amet, consectetur adipi scing elit, sed do eiusmod tempolabor</p></article>
  <div class="post-thumb" role="img" aria-label="Glowing blue fibre optic strands" style="top:4334px;background:radial-gradient(circle,#8fe0ff,#1f5fb0 60%,#0d1d45)"></div>
  <article class="post" style="top:4504px"><h5>Lorem ipsum dolor sit amet, consectetur</h5><p>Lorem ipsum dolor sit amet, consectetur adipi scing elit, sed do eiusmod tempolabor</p></article>
  <div class="post-thumb" role="img" aria-label="Server rack with status lights" style="top:4508px;background:linear-gradient(135deg,#3a4f8a,#1c2a55 55%,#a33)"></div>
</section>

<!-- Footer -->
<footer>
  <div class="abs" style="left:0;top:4760px;width:1200px;height:559px;background:var(--navy)"></div>
  <svg class="abs" style="left:0;top:4755px" width="1200" height="70" aria-hidden="true">
    <polygon points="0,0 1200,0 1200,8 0,28" fill="#fff"/>
    <polygon points="380,22 1200,8 1200,40" fill="var(--red)"/>
  </svg>

  <h3 class="foot-h" style="left:149px;top:4898px">Contact</h3>
  <div class="field" style="left:149px;top:4948px;width:182px;height:41px">Name</div>
  <div class="field" style="left:336px;top:4948px;width:181px;height:41px">Phone</div>
  <div class="field" style="left:149px;top:4999px;width:368px;height:40px">Email</div>
  <div class="field" style="left:149px;top:5049px;width:368px;height:99px">Message</div>
  <a class="btn" style="left:149px;top:5167px;width:130px;height:43px;font-size:16px">Submit</a>

  <h3 class="foot-h" style="left:638px;top:4898px">Location</h3>
  <svg class="abs" style="left:638px;top:4946px" width="14" height="18" aria-hidden="true"><path d="M7,0 A7,7 0 0 1 14,7 C14,12 7,18 7,18 C7,18 0,12 0,7 A7,7 0 0 1 7,0Z" fill="var(--red-bright)"/><circle cx="7" cy="7" r="2.5" fill="var(--navy)"/></svg>
  <div class="foot-small" style="left:664px;top:4943px">48 Copperline Road<br>Suite 210, Marrow Square<br>Eastbrook, TN 37990</div>
  <svg class="abs" style="left:638px;top:5009px" width="14" height="14" aria-hidden="true"><path d="M3,0 L6,4 L4,6 Q6,9 8,10 L10,8 L14,11 L12,14 Q5,14 0,3 Z" fill="var(--red-bright)"/></svg>
  <div class="foot-small" style="left:664px;top:5006px">Contact<br>(555) 014-2290<br>(555) 014-2291 (fax)</div>
  <svg class="abs" style="left:638px;top:5077px" width="14" height="11" aria-hidden="true"><rect width="14" height="11" fill="var(--red-bright)"/><path d="M0,0 L7,6 L14,0" stroke="var(--navy)" fill="none"/></svg>
  <div class="foot-small" style="left:664px;top:5073px">Email:<br>office@halvernlink.example</div>

  <h3 class="foot-h" style="left:958px;top:4898px">Links</h3>
  <ul class="links"><li>Home</li><li>About Us</li><li>Products</li><li>Our team</li><li>News</li><li>Blog Posts</li><li>Testimonials</li><li>Contact</li></ul>

  <h3 class="foot-h" style="left:958px;top:5152px">Follow</h3>
  <span class="social" style="left:958px"></span>
  <span class="social" style="left:1001px"></span>
  <span class="social" style="left:1040px"></span>

  <div class="brand" style="left:0;width:1200px;justify-content:center;top:5182px;font-size:14px;color:#fff"><span class="mark" style="width:14px;height:14px"></span>Halvern Link Works</div>
  <p class="abs" style="left:0;width:1200px;top:5268px;text-align:center;color:#fff;font-size:11px">©2022 HALVERN LINK WORKS. ALL RIGHTS RESERVED.</p>

  <div class="abs" style="left:1140px;top:4946px;width:60px;height:151px;background:var(--red-bright);border-radius:8px 0 0 8px"></div>
  <div class="abs" style="left:1140px;top:4946px;width:60px;height:105px;display:flex;align-items:center;justify-content:center"><span style="transform:rotate(-90deg);white-space:nowrap;color:#fff;font-weight:700;font-size:14px">LIVE CHAT</span></div>
  <svg class="abs" style="left:1155px;top:5060px" width="30" height="28" aria-hidden="true"><path d="M15,2 C23,2 28,7 28,13 C28,19 23,23 15,23 L8,27 L9,21 C4,19 2,16 2,13 C2,7 7,2 15,2Z" fill="#fff"/><circle cx="10" cy="13" r="1.8" fill="var(--red-bright)"/><circle cx="15" cy="13" r="1.8" fill="var(--red-bright)"/><circle cx="20" cy="13" r="1.8" fill="var(--red-bright)"/></svg>
</footer>

</body>
</html>
```